Anzeigengestaltung für Bestattungsunternehmen
Sehr gute Arbeit. Alle Designs von diesem Designer waren die mit Abstand besten welche auch die Wünsche von uns am besten umgesetzt hat. Zum Schluss selbstständig nochmal ein weiteres Design eingereicht welches nochmal etwas heller und freundlicher war - Am Ende wollten wir nur noch ein anderes Bild in der Anzeige haben, dies wurde sogar am Abend noch gemacht innerhalb von einer Stunde. Sehr gute Kommunikation und vor allem sehr gute schnelle Umsetzung
Zielgruppe
Vaselund Bestattungen bietet bundesweit Bestattungen zu sehr günstigen Preisen ein.
Aufgabenstellung
In die Anzeige soll neben dem Logo sowie unsere Website (www.bestatter-vaselund-beispiel.de) auch die folgenden Infor:
Moorkamp 24 - 23861 Sülfeld
Weidenstr. 17 - 22089 Hamburg
Lübbecker Str. - 22147 Hamburg
Unser Slogan:
Verlässlich. Respektvoll. Fair.
,,Komplettbestattung ab 850 € inkl. MwSt.''
Nur wenn möglich und es noch ,,passend aussieht'' den Textr
Die gute Alternative zu anderen Bestattern....
einfügen.
Es soll in den passenden hellen Farben zu unserem Logo sein, die Anzeige soll nicht dunkel sondern hell und freundlich sein. Die Anzeige wird eine Seite in einem regionalen Heft einnehmen (DIN a5)

```html
<!DOCTYPE html>
<html lang="de">
<head>
<meta charset="utf-8">
<title>Vaselund Bestattungen – Anzeige</title>
<link rel="stylesheet" href="https://fonts.googleapis.com/css2?family=Open+Sans:wght@400;600;700&display=swap">
<style>
  :root {
    --green: #64b22e;
    --grey: #555555;
    --ink: #1e1e1e;
    --paper: #ffffff;
  }
  html, body {
    margin: 0;
    padding: 0;
    overflow: hidden;
    background: var(--paper);
  }
  .ad {
    position: relative;
    width: 899px;
    height: 1200px;
    overflow: hidden;
    background: var(--paper);
    font-family: "Open Sans", Arial, sans-serif;
    color: var(--ink);
  }
  .ad__shapes {
    position: absolute;
    inset: 0;
    width: 899px;
    height: 1200px;
  }
  .brand {
    position: absolute;
    left: 50px;
    top: 56px;
    color: var(--grey);
    font-weight: 600;
  }
  .brand__name {
    display: block;
    font-size: 50px;
    line-height: 1;
  }
  .brand__trade {
    display: block;
    margin-top: 8px;
    margin-left: 68px;
    font-size: 14px;
    line-height: 1;
    letter-spacing: 4.5px;
  }
  .brand__dot {
    position: absolute;
    left: 296px;
    top: 22px;
    width: 84px;
    height: 84px;
    border-radius: 50%;
    background: var(--green);
  }
  .slogan {
    position: absolute;
    left: 0;
    right: 0;
    top: 660px;
    margin: 0;
    text-align: center;
    color: var(--green);
    font-size: 54px;
    line-height: 66px;
    font-weight: 700;
    letter-spacing: -0.5px;
  }
  .intro {
    position: absolute;
    left: 66px;
    top: 758px;
    margin: 0;
    font-size: 31px;
    line-height: 42px;
  }
  .locations {
    position: absolute;
    right: 64px;
    top: 759px;
    margin: 0;
    padding: 0;
    list-style: none;
    text-align: right;
    font-size: 31px;
    line-height: 42px;
  }
  .locations li { margin-bottom: 29px; }
  .locations li::before {
    content: "";
    display: inline-block;
    width: 10px;
    height: 10px;
    border-radius: 50%;
    background: var(--green);
    margin-right: 12px;
    vertical-align: middle;
  }
  .price {
    position: absolute;
    left: 66px;
    top: 878px;
    width: 423px;
    height: 239px;
    border-radius: 50%;
    background: var(--green);
    color: var(--paper);
    text-align: center;
    display: flex;
    flex-direction: column;
    justify-content: center;
    font-size: 29px;
    line-height: 54px;
  }
  .price__amount {
    font-size: 50px;
    line-height: 56px;
  }
  .price__amount small { font-size: 29px; }
  .website {
    position: absolute;
    right: 64px;
    top: 1157px;
    color: var(--paper);
    font-size: 25px;
    line-height: 30px;
    letter-spacing: 0.5px;
  }
</style>
</head>
<body>
<main class="ad">
  <svg class="ad__shapes" viewBox="0 0 1400 1985" preserveAspectRatio="none">
    <defs>
      <linearGradient id="photoTone" x1="0" y1="0" x2="1" y2="0.3">
        <stop offset="0" stop-color="#3a1c18"/>
        <stop offset="0.25" stop-color="#2d2a20"/>
        <stop offset="0.5" stop-color="#9b958c"/>
        <stop offset="0.75" stop-color="#dedbd5"/>
        <stop offset="1" stop-color="#ecebe7"/>
      </linearGradient>
    </defs>
    <path class="hero-photo" role="img" aria-label="Foto: rote Rosen mit Efeu auf weißen Kieselsteinen und ein Steinherz mit Gedenkspruch"
          d="M0,490 Q600,170 1400,100 L1400,1080 Q700,1040 0,760 Z" fill="url(#photoTone)"/>
    <path class="hero-edge" d="M0,490 Q600,170 1400,100" fill="none" stroke="var(--green)" stroke-width="14"/>
    <path class="hero-edge" d="M0,760 Q700,1040 1400,1080" fill="none" stroke="var(--green)" stroke-width="6"/>
    <path class="footer-swoosh" d="M260,1880 Q900,1935 1400,1795 L1400,1830 Q850,1975 260,1880 Z" fill="var(--grey)"/>
    <path class="footer-band" d="M0,1845 Q300,1935 600,1935 Q1000,1930 1400,1830 L1400,1985 L0,1985 Z" fill="var(--green)"/>
  </svg>

  <header class="brand">
    <span class="brand__name">Vaselund</span>
    <span class="brand__trade">BESTATTUNGEN</span>
  </header>
  <span class="brand__dot" aria-hidden="true"></span>

  <h1 class="slogan">Verlässlich. Respektvoll. Fair.</h1>

  <p class="intro">Die gute Alternative<br>zu anderen Bestattern</p>

  <ul class="locations">
    <li>Moorkamp 24<br>23861 Sülfeld</li>
    <li>Weidenstr. 17<br>22089 Hamburg</li>
    <li>Lübbecker Str.<br>22147 Hamburg</li>
  </ul>

  <div class="price">
    <span>KOMPLETTBESTATTUNG</span>
    <span class="price__amount"><small>AB</small> 850 €</span>
    <span>INKL. MWST.</span>
  </div>

  <span class="website">www.bestatter-vaselund-beispiel.de</span>
</main>
</body>
</html>
```